Need a Middle Eastern/Cooking/Nutrition Design please :)

Hi I am looking to revamp my Middle Eastern/Cooking/Nutrition Blog for something that is clean, sophisticated yet sultry. My site now www.flavorsofthedunes.com is messy and needs more color help with background. Please send anything you think is suitable for the concept.
Target Market(s)
high end
Industry/Entity Type
Nutrition
Requirements
Must have
- Your work looks wonderful!
I am looking forward to your designs! I am really trying to revamp my current site www.flavorsofthedunes.com to be more clean and sophisticated.
I like this color palette or maybe royal purple and gold. http://www.huegatherers.net/palette/412907/The_Desert_Dusk
I had my website evaluated by a brand specialist and this what she said I should be doing :) Let me know what you think- really appreciate it!
Comments Below:
Given your brand identity, I think you want to go for something clean and simple but with touches of bold color and iconography. You want the site to come off as approachable, but to also have an exotic and slightly mysterious edge. Perhaps choose a solid background color and use stylish icons, flourishes and images to bring the Middle Eastern/Mediterranean flavor.
I also recommend that you use a neutral color or a whitewashed design as your background. It is easier on the eyes to read a lot of text when it’s a neutral (light or white) background color with a darker font.
Here is a color palette that I like for you: http://www.huegatherers.net/palette/412907/The_Desert_Dusk
In terms of organization, I think it would be great to have your home page be a jump page. So, rather than having a list of your recent posts, perhaps you can welcome guests with a picture of yourself/your food/your brand.
Then, you could have a menu of options for people to explore your site (kind of like the bar you have at the top of your page now). But instead of just having the text, you could use images as the links to the different pages. This would include a link to classes, recipes, nutritional information, products, TV shows/videos, bio, etc. And you could organize it in a creative way on the page.
There are so many ways that you can organize your site, and it’s completely up to you! But here are some examples that I think you could look to for inspiration:
http://lorenabrevicelli.com/
http://www.sunlitmarquise.com/
http://www.dybelin.com/
http://www.trylentilo.com/trylentilo.com/Lentilo.html
http://www.korubrisk.com/
http://www.velukebab.com/
For your brand name, ultimately, you want something that reflects the down to earth yet somewhat exotic nature of your brand. The actual brand name is up to you…but I do like where you’re going with the ingredients.
I want simple and sophisticated yet also portrays the mysterious and exotic Middle East. The site colors and pictures should transport people but also want it clean. I think my site is too busy now.
The content and layout could be the same but the logo, domain name possible and website name, background and color scheme all have to change although I do like dark purple and gold as possibilities along with the color pattern I sent already,
Im not sure if its a single page or full project but I do want a total revamp of the scheme- do you need to redo the website or just remake the existing because I can provide the website info if thats the case . I can pay the up front cost now. I believe the quote is 300.
Also im not sure if I should stick with the Sumac up name or here are other name options if you think they meet the sophisticated brand of the Middle East more.
tahini & honey
fig & chickpea
saffron & rosewater- very exotic
sesame & quince
pomegranates & pistachios
saffron & pomegranates
figs & saffron
The name should be playful and fun for the site. I like the idea of ingredients because it brings both the Mediterranean and Middle East imagery and allows for broad appeal.
Thank you soooooooooo much- I know it’s a lot to think about and I greatly appreciate your insight and talents in this!!
Nice to have
- Clean, sophisticated, sultry, exotic and professional
Should not have
- too busy

```html
<!DOCTYPE html>
<html lang="en">
<head>
<meta charset="utf-8">
<title>sesame &amp; quince — Tastes of Turkey &amp; the Middle East</title>
<link href="https://fonts.googleapis.com/css2?family=Arimo:wght@400;700&display=swap" rel="stylesheet">
<style>
  :root{
    --plum:#4a1a50;
    --plum-text:#5a2160;
    --gold:#d4a84b;
    --gold-light:#f3d36b;
    --coral:#f07272;
    --cream:#fbf8e4;
    --sand:#f1dba6;
    --paper:#ffffff;
    --rule:#d8d2b8;
    --photo-red:#c8412e;
    --photo-plate:#f2eee8;
  }
  *{box-sizing:border-box;margin:0;padding:0}
  html,body{width:1200px;height:2225px;overflow:hidden}
  body{
    background:linear-gradient(90deg,#f0d7a0 0,#f6e6bd 6%,var(--sand) 100%);
    font-family:"Arimo",Arial,sans-serif;color:var(--plum-text);
    position:relative;
  }
  .page{position:absolute;left:77px;top:0;width:1046px;height:2225px;background:var(--cream)}
  .abs{position:absolute}

  .brand{left:0;width:1200px;top:38px;text-align:center}
  .brand-name{font-family:"Arimo",Arial,sans-serif;font-weight:400;font-size:46px;color:var(--plum);letter-spacing:2px;line-height:1}
  .brand-tag{margin-top:14px;font-size:17px;color:var(--gold);letter-spacing:.5px;text-transform:uppercase}

  .main-nav{left:95px;top:154px;width:1012px;height:48px;background:var(--plum);
    display:flex;align-items:center;justify-content:space-between;padding:0 14px}
  .main-nav a{color:var(--gold-light);text-decoration:none;font-size:16px;text-transform:uppercase}

  .hero{left:95px;top:229px;width:1012px;height:393px;background:var(--coral);padding:14px}
  .photo{background:radial-gradient(ellipse at 62% 40%,#e06a3c 0,var(--photo-red) 28%,#a5332a 42%,var(--photo-plate) 60%,#f7f5f1 100%)}
  .hero .photo{width:100%;height:100%}

  .intro-text{left:116px;top:678px;width:660px;font-size:15px;line-height:26px;color:var(--plum-text)}
  .more-link{font-size:11px;font-weight:700;letter-spacing:1.5px;color:var(--plum);text-transform:uppercase}
  .intro-more{left:716px;top:776px}
  .portrait-frame{left:826px;top:644px;width:281px;height:171px;border:1px solid var(--gold);padding:11px;background:var(--paper)}
  .portrait-frame .photo{width:100%;height:100%;background:linear-gradient(90deg,#2a4bb0 0,#5f7fd6 45%,#c9b8a8 60%,#e8e8f2 100%)}
  .divider{left:95px;top:831px;width:1012px;height:5px;border-top:2px dashed #c8c1a8;border-bottom:2px dashed #c8c1a8}

  .post{left:95px;width:701px;height:357px;background:var(--paper);border:1px solid var(--rule)}
  .post-title{position:absolute;left:20px;top:18px;font-size:27px;font-weight:400;color:var(--plum)}
  .post-meta{position:absolute;left:17px;top:62px;width:666px;height:33px;background:var(--gold);
    display:flex;align-items:center;justify-content:space-between;padding:0 16px 0 6px;font-size:13px;color:#3a1a3e}
  .post-meta .comments{display:flex;align-items:center;gap:14px}
  .post-thumb{position:absolute;left:17px;top:116px;width:222px;height:170px}
  .post-excerpt{position:absolute;left:257px;top:112px;width:405px;font-size:13.5px;line-height:22.7px;color:var(--plum-text)}
  .post-foot{position:absolute;left:17px;top:313px;width:666px;border-top:1px solid var(--rule);
    display:flex;align-items:center;justify-content:space-between;padding:10px 22px 0 6px;font-size:13px}
  .share{display:flex;align-items:center;gap:12px}
  .share-box{width:26px;height:26px;border-radius:4px}
  .share-a{background:#3b5a9a}.share-b{background:#3fa6c9}

  .side-box{left:819px;width:288px}
  .subscribe{top:864px;height:143px;background:var(--coral);padding:14px 18px}
  .subscribe h3{font-size:17px;font-weight:400;color:#fff}
  .sub-field{margin-top:12px;height:37px;background:#fff;border-radius:3px;position:relative}
  .sub-field svg{position:absolute;right:10px;top:9px}
  .sub-icons{margin-top:12px;display:flex;justify-content:center;gap:20px}
  .sub-icons span{width:40px;height:40px;border-radius:6px;border:2px solid #f5c4a8}
  .sub-icons .i1{background:#e8a040}.sub-icons .i2{background:#3b5a9a}.sub-icons .i3{background:#3fa6c9}

  .purple-box{background:var(--plum);padding:0 14px}
  .purple-box h3{font-weight:400;font-size:17px;color:var(--gold-light);text-align:center;line-height:23px}
  .purple-box .photo{width:260px;height:107px;margin:0 auto}
  .purple-box p{font-size:13px;line-height:21px;color:#fff;padding:0 14px 0 6px}
  .btn-more{position:absolute;right:18px;width:74px;height:22px;background:var(--gold-light);color:var(--plum);
    font-size:11px;display:flex;align-items:center;justify-content:center;gap:8px}
  .product-label{background:linear-gradient(90deg,#8a4aa0 0,#b98fca 8%,#efe6c8 14%,#f3ecd2 86%,#b98fca 92%,#8a4aa0 100%)}

  .pager{left:265px;top:2032px;display:flex;align-items:center;font-size:15px;color:var(--plum)}
  .pager span{display:inline-flex;align-items:center;justify-content:center;height:32px}
  .pager .num{width:50px}
  .pager .current{width:32px;background:var(--gold);margin:0 9px}
  .pager .prev{width:75px;margin-right:30px}.pager .next{width:60px;margin-left:30px}

  .footer{left:77px;top:2167px;width:1046px;border-top:1px solid var(--rule);text-align:center;padding-top:16px;font-size:13px;color:var(--plum)}
</style>
</head>
<body>
<div class="page"></div>

<header class="abs brand">
  <div class="brand-name">sesame &amp; quince</div>
  <div class="brand-tag">Tastes of Turkey &amp; the Middle East</div>
</header>

<nav class="abs main-nav">
  <a href="#">Home</a><a href="#">Why Mediterranean &amp; Mideast Cuisine?</a><a href="#">Cooking Class</a><a href="#">Healthy Recipes</a><a href="#">About</a><a href="#">Contact</a>
</nav>

<section class="abs hero"><div class="photo" role="img" aria-label="Close-up of roasted stuffed tomato with herbs and sauce on a white plate"></div></section>

<p class="abs intro-text">This website is about me sharing how to be fit and full Mediterranean style by sharing healthy Mediterranean recipes and inspiring others with the wise Mediterranean lifestyle motto to: savor food and savor life! I got inspired to do this website by my family- and I mean everyone in it (including the semi-annoying members).</p>
<span class="abs more-link intro-more">[ Read More ]</span>
<div class="abs portrait-frame"><div class="photo" role="img" aria-label="Portrait of the blog author by the sea"></div></div>
<div class="abs divider"></div>

<article class="abs post" style="top:864px">
  <h2 class="post-title">Fall Butternut Squash with Homemade Harissa</h2>
  <div class="post-meta"><span>Posted on October 11, 2011 in: Healthy Recipes</span><span class="comments"><svg width="22" height="20" viewBox="0 0 22 20"><ellipse cx="9" cy="8" rx="8" ry="6.5" fill="#4a1a50"/><ellipse cx="15" cy="12" rx="6" ry="5" fill="#4a1a50"/></svg>0 comments</span></div>
  <div class="post-thumb photo" role="img" aria-label="Roasted butternut squash stack with harissa"></div>
  <p class="post-excerpt">When its fall, I love buying squash from the market and feeling like I am all ready for the new season even though I have no idea what I am going to be doing with the squash right then and there. But this recipe is my go to for a decadent feast of butternut squash and being so tasty, its a great way to embark on an amazing fall. I love butternut squash particularly roasted because you get the natural caramelization from the natural sugars in the squash to come out.</p>
  <div class="post-foot"><span class="share">Share it: <span class="share-box share-a"></span><span class="share-box share-b"></span></span><span class="more-link">[ Read More ]</span></div>
</article>

<article class="abs post" style="top:1246px">
  <h2 class="post-title">Fall Butternut Squash with Homemade Harissa</h2>
  <div class="post-meta"><span>Posted on October 11, 2011 in: Healthy Recipes</span><span class="comments"><svg width="22" height="20" viewBox="0 0 22 20"><ellipse cx="9" cy="8" rx="8" ry="6.5" fill="#4a1a50"/><ellipse cx="15" cy="12" rx="6" ry="5" fill="#4a1a50"/></svg>0 comments</span></div>
  <div class="post-thumb photo" role="img" aria-label="Roasted butternut squash stack with harissa"></div>
  <p class="post-excerpt">When its fall, I love buying squash from the market and feeling like I am all ready for the new season even though I have no idea what I am going to be doing with the squash right then and there. But this recipe is my go to for a decadent feast of butternut squash and being so tasty, its a great way to embark on an amazing fall. I love butternut squash particularly roasted because you get the natural caramelization from the natural sugars in the squash to come out.</p>
  <div class="post-foot"><span class="share">Share it: <span class="share-box share-a"></span><span class="share-box share-b"></span></span><span class="more-link">[ Read More ]</span></div>
</article>

<article class="abs post" style="top:1629px">
  <h2 class="post-title">Fall Butternut Squash with Homemade Harissa</h2>
  <div class="post-meta"><span>Posted on October 11, 2011 in: Healthy Recipes</span><span class="comments"><svg width="22" height="20" viewBox="0 0 22 20"><ellipse cx="9" cy="8" rx="8" ry="6.5" fill="#4a1a50"/><ellipse cx="15" cy="12" rx="6" ry="5" fill="#4a1a50"/></svg>0 comments</span></div>
  <div class="post-thumb photo" role="img" aria-label="Roasted butternut squash stack with harissa"></div>
  <p class="post-excerpt">When its fall, I love buying squash from the market and feeling like I am all ready for the new season even though I have no idea what I am going to be doing with the squash right then and there. But this recipe is my go to for a decadent feast of butternut squash and being so tasty, its a great way to embark on an amazing fall. I love butternut squash particularly roasted because you get the natural caramelization from the natural sugars in the squash to come out.</p>
  <div class="post-foot"><span class="share">Share it: <span class="share-box share-a"></span><span class="share-box share-b"></span></span><span class="more-link">[ Read More ]</span></div>
</article>

<aside>
  <div class="abs side-box subscribe">
    <h3>Subscribe to our mailing list</h3>
    <div class="sub-field"><svg width="20" height="20" viewBox="0 0 20 20"><path d="M5 2 L15 10 L5 18" fill="none" stroke="#e0b53f" stroke-width="4"/></svg></div>
    <div class="sub-icons"><span class="i1"></span><span class="i2"></span><span class="i3"></span></div>
  </div>

  <div class="abs side-box purple-box" style="top:1034px;height:295px">
    <h3 style="padding-top:12px">Suggestion and Question Box</h3>
    <div class="photo" role="img" aria-label="Plated roasted vegetable dish" style="margin-top:14px"></div>
    <p style="margin-top:14px">If you have a suggestion for a recipe or any questions, we would be glad to hear it! Just write it in the box and hit submit :)</p>
    <span class="btn-more" style="top:260px">MORE <b>&gt;&gt;</b></span>
  </div>

  <div class="abs side-box purple-box" style="top:1352px;height:313px">
    <h3 style="padding-top:12px">Benefits of Middle Eastern &amp;<br>Mediterranean Cuisine</h3>
    <div class="photo" role="img" aria-label="Plated roasted vegetable dish" style="margin-top:10px"></div>
    <p style="margin-top:14px">There really is a delicious way to be fit, full and healthy! Much research and studies have been done on the benefits of the Mediterranean cuisine.</p>
    <span class="btn-more" style="top:280px">MORE <b>&gt;&gt;</b></span>
  </div>

  <div class="abs side-box purple-box" style="top:1688px;height:316px">
    <h3 style="padding-top:14px">Nadia's Doré Levant<br>Gourmet Products in Stores</h3>
    <div class="photo product-label" role="img" aria-label="Gourmet baklava product label" style="margin-top:12px"></div>
    <p style="margin-top:14px">There really is a delicious way to be fit, full and healthy! Much research and studies have been done on the benefits of the Mediterranean cuisine.</p>
    <span class="btn-more" style="top:282px">MORE <b>&gt;&gt;</b></span>
  </div>
</aside>

<nav class="abs pager">
  <span class="prev">Previous</span><span class="current">1</span><span class="num">2</span><span class="num">3</span><span class="num">4</span><span class="num">5</span><span class="next">Next</span>
</nav>

<footer class="abs footer">Copyright © 2012 sesame &amp; quince</footer>
</body>
</html>
```